IT support company needs Banner Ad for the top of their quote layout template

We need a banner Ad for the top of our for quote layout template so it is sent out on all our quotes

The banner size must be 827 x 100 pixels - anything larger than 60 KB can cause upload time issues

We have attached our logo and examples of the quote page to see how it looks in the context of the whole page.

Essential elements of the banner
- Must have our logo but this can be changed to be different colours if it makes the design work better i.e. Tidal Grove could be all in white

Colours
- Can use all of our standard colours - Orange, Black, Grey and White

Images
- As a premium IT support company we deal with people and technology so would like to see both of these Incorporated into the banner i.e. people using technology These images could be watermarked or one colour effect.

Look and Feel
- Professional, friendly, people, technology, premium

Target Market
Small business owners and managers

Industry/Entity Type

It Company

```html
<!DOCTYPE html>
<html lang="nl">
<head>
<meta charset="utf-8">
<title>Standard MSP #2 – Offerte</title>
<link href="https://fonts.googleapis.com/css2?family=Carlito:wght@400;700&display=swap" rel="stylesheet">
<style>
  :root {
    --orange: #e8620e;
    --orange-light: #f6a055;
    --orange-dark: #c4500c;
    --heading-orange: #c0500f;
    --black: #1b1b1b;
    --charcoal: #2c2c2c;
    --text: #111111;
    --white: #ffffff;
  }
  * { box-sizing: border-box; margin: 0; padding: 0; }
  html, body { width: 1200px; height: 612px; overflow: hidden; background: var(--white); }
  body { position: relative; font-family: "Carlito", "Calibri", sans-serif; color: var(--text); }

  .banner { position: absolute; left: 0; top: 0; width: 1200px; height: 147px; }
  .brand {
    position: absolute; left: 28px; top: 50px;
    font-size: 38px; font-weight: 700; letter-spacing: 1px;
    color: var(--white); line-height: 1;
  }

  .quote-title { position: absolute; left: 40px; top: 196px; font-size: 28px; font-weight: 400; }

  .portrait {
    position: absolute; left: 38px; top: 251px; width: 141px; height: 188px;
    background: linear-gradient(180deg, #8a8a8a 0%, #5e5e5e 55%, #3a3a3a 100%);
  }

  .info-col { position: absolute; top: 251px; font-size: 18px; line-height: 24.5px; }
  .info-col h2 { font-size: 22px; font-weight: 400; color: var(--heading-orange); margin-bottom: 11px; line-height: 24px; }
  .info-col .strong { font-weight: 700; }
  .info-col .gap { height: 24.5px; }
  .col-from { left: 196px; }
  .col-for { left: 523px; }
  .col-details { left: 910px; }

  .divider { position: absolute; left: 37px; top: 456px; width: 1124px; height: 4px; background: var(--orange-dark); }

  .summary-title { position: absolute; left: 40px; top: 487px; font-size: 25px; font-weight: 400; }

  .summary-table {
    position: absolute; left: 37px; top: 525px; width: 1124px;
    border-collapse: collapse; font-size: 18px; border: 2px solid var(--black);
  }
  .summary-table th, .summary-table td { height: 37px; padding: 0 8px; border: 1.5px solid var(--black); }
  .summary-table th {
    font-weight: 400; text-align: left;
    background: linear-gradient(90deg, #f4b888 0%, #fce6d6 50%, #f6c39c 100%);
  }
  .summary-table .amount { width: 157px; text-align: right; }
</style>
</head>
<body>

<svg class="banner" viewBox="0 0 1200 147" xmlns="http://www.w3.org/2000/svg">
  <defs>
    <linearGradient id="bandGrad" x1="0" x2="1" y1="0" y2="0">
      <stop offset="0" stop-color="#f08a30"/>
      <stop offset="0.5" stop-color="#e8620e"/>
      <stop offset="1" stop-color="#d4550a"/>
    </linearGradient>
    <linearGradient id="photoGrad" x1="0" x2="1" y1="0" y2="1">
      <stop offset="0" stop-color="#d9dde0"/>
      <stop offset="0.45" stop-color="#eef0f1"/>
      <stop offset="1" stop-color="#b9c0c6"/>
    </linearGradient>
  </defs>
  <rect width="1200" height="147" fill="var(--black)"/>
  <rect x="0" y="130" width="1200" height="17" fill="url(#bandGrad)"/>
  <polygon points="330,75 420,0 1200,0 1200,147 420,147" fill="var(--orange)"/>
  <polygon points="420,75 500,6 1120,6 1190,75 1120,141 500,141" fill="var(--charcoal)"/>
  <polygon points="428,75 505,8 1112,8 1180,75 1112,139 505,139"
           fill="url(#photoGrad)" role="img"
           aria-label="Photo of support staff with headsets working at computers in an office"/>
  <polygon points="735,0 775,0 725,147 685,147" fill="var(--charcoal)"/>
  <polygon points="1200,0 1200,147 1110,75" fill="var(--orange)"/>
</svg>
<div class="brand">TIDAL GROVE</div>

<h1 class="quote-title">Standard MSP&nbsp; #2</h1>

<div class="portrait" role="img" aria-label="Portrait photo of the account manager"></div>

<section class="info-col col-from">
  <h2>Opgesteld door:</h2>
  <p class="strong">Marcus Hale Inc</p>
  <p>Marcus Hale</p>
  <div class="gap"></div>
  <p>Fax</p>
  <p>marcus.hale@northlane.com</p>
</section>

<section class="info-col col-for">
  <h2>Opgesteld voor:</h2>
  <p class="strong">Copper Ridge</p>
  <p>2718 Alder Rd.</p>
  <p>Fairview,&nbsp;&nbsp; 55208</p>
  <p>Laura Brenner</p>
  <p>tom.fenwick@bluefern.co.uk</p>
</section>

<section class="info-col col-details">
  <h2>Gegevens Offerte:</h2>
  <p class="strong">Offerte #: TG-004173</p>
  <p>Versie: 1</p>
  <p>Leverdatum: 14/11/2017</p>
  <p>Vervaldatum: 31/12/2017</p>
</section>

<div class="divider"></div>

<h2 class="summary-title">Overzicht Offerte</h2>

<table class="summary-table">
  <thead>
    <tr><th>Beschrijving</th><th class="amount">Bedrag</th></tr>
  </thead>
  <tbody>
    <tr><td>Initial Investment</td><td class="amount">$800.00</td></tr>
  </tbody>
</table>

</body>
</html>
```